https://dorvakel.com

We need a cool technology design for our Managed IT Services company. We are located in Coral Springs Florida. We provide all IT services and support for small to medium sized businesses. We would like to see designs that use our blue and white colors from our website.

```html
<!DOCTYPE html>
<html lang="en">
<head>
<meta charset="utf-8">
<title>Dorvakel Business Cards</title>
<link rel="stylesheet" href="https://fonts.googleapis.com/css2?family=Oxygen:wght@400;700&display=swap">
<style>
  :root {
    --navy: #132c52;
    --paper: #f1f2f2;
    --bg: #dcdcdc;
    --soft-text: #b9c3d6;
    --ink: #132c52;
  }
  * { margin: 0; padding: 0; box-sizing: border-box; }
  html, body { width: 1200px; height: 1200px; overflow: hidden; }
  body {
    background: var(--bg);
    font-family: "Oxygen", "Verdana", sans-serif;
    position: relative;
  }
  .card {
    position: absolute;
    left: 320px;
    width: 560px;
    height: 320px;
    overflow: hidden;
    box-shadow: 0 2px 8px rgba(0,0,0,0.12);
  }
  .card--front { top: 190px; display: flex; }
  .card--back { top: 690px; background: var(--navy); }

  .front__brand {
    width: 280px;
    background: var(--navy);
    display: flex;
    align-items: center;
    justify-content: center;
  }
  .brand-name {
    font-weight: 700;
    letter-spacing: 1px;
    line-height: 1;
  }
  .front__brand .brand-name { color: #ffffff; font-size: 40px; }

  .front__contact {
    flex: 1;
    background: var(--paper);
    padding: 40px 30px 0 34px;
  }
  .front__contact .brand-name { color: var(--ink); font-size: 28px; margin-bottom: 26px; }
  .contact-list { list-style: none; color: var(--ink); font-size: 12.5px; line-height: 1.35; }
  .contact-item { display: flex; align-items: center; gap: 12px; margin-bottom: 12px; }
  .contact-icon {
    width: 20px; height: 20px; flex: none;
    border: 1.6px solid var(--ink); border-radius: 50%;
    display: flex; align-items: center; justify-content: center;
  }
  .contact-icon svg { width: 11px; height: 11px; fill: var(--ink); }

  .back__url {
    position: absolute;
    left: 40px;
    bottom: 42px;
    color: var(--soft-text);
    font-size: 30px;
    letter-spacing: 0.5px;
  }
</style>
</head>
<body>
  <section class="card card--front">
    <div class="front__brand">
      <span class="brand-name">DORVAKEL</span>
    </div>
    <div class="front__contact">
      <div class="brand-name">DORVAKEL</div>
      <ul class="contact-list">
        <li class="contact-item">
          <span class="contact-icon"><svg viewBox="0 0 12 12"><path d="M6 0a4 4 0 0 0-4 4c0 3 4 8 4 8s4-5 4-8a4 4 0 0 0-4-4zm0 5.5A1.5 1.5 0 1 1 6 2.5a1.5 1.5 0 0 1 0 3z"/></svg></span>
          <span>2780 Palmetto Way #410<br>Coral Springs, Florida 33065</span>
        </li>
        <li class="contact-item">
          <span class="contact-icon"><svg viewBox="0 0 12 12"><path d="M2.5 1 4.5 3 3.5 4.5c.7 1.6 2 2.9 3.6 3.6L8.6 7l2 2-1.2 1.8C5.3 10.5 1.5 6.7 1 2.4z"/></svg></span>
          <span>(954) 555-0142</span>
        </li>
        <li class="contact-item">
          <span class="contact-icon"><svg viewBox="0 0 12 12"><path d="M6 1a5 5 0 1 0 2.6 9.3l-.5-.9A4 4 0 1 1 10 6v.6c0 .6-.4 1-.9 1s-.9-.4-.9-1V3.5h-1v.4A2.4 2.4 0 1 0 8 7.5 1.9 1.9 0 0 0 11 6.6V6a5 5 0 0 0-5-5zm0 6.4A1.4 1.4 0 1 1 6 4.6a1.4 1.4 0 0 1 0 2.8z"/></svg></span>
          <span>https://dorvakel.com</span>
        </li>
      </ul>
    </div>
  </section>

  <section class="card card--back">
    <span class="back__url">https://dorvakel.com</span>
  </section>
</body>
</html>
```